Robotic Physical Therapy office needs a Grand Opening Flyer

We need a Grand Opening flyer design for a robotic physical therapy office named Stellar Motion Therapy. We would like it to have a clean, classy, upscale feeling that gives potential clients a V.I.P. feeling. We would like to use the colors black, gray, and yellow (logo will be uploaded).

Event: Thursday, June 1st, 2023 from 12pm-6pm
location: 58274 Harlow Ave, Bloomfield Hills, MI 48319

Industry/Entity Type

Physical therapy

Font styles to use
Script

Colors

Designer to choose colors to be used in the design.

Requirements
Nice to have
• More of a vip feel for the invite

```html
<!DOCTYPE html>
<html lang="en">
<head>
<meta charset="utf-8">
<title>Stellar Motion Therapy – Grand Opening</title>
<link rel="stylesheet" href="https://fonts.googleapis.com/css2?family=Bebas+Neue&family=Playball&display=swap">
<style>
  :root {
    --stage: #8c8c8c;
    --paper: #fbfbfc;
    --paper-shade: #eff0f2;
    --ink: #25252e;
    --gold: #e9c61f;
    --gold-soft: #f3df7a;
    --gold-deep: #d4a91a;
    --rule: #e2cd63;
  }
  * { box-sizing: border-box; margin: 0; padding: 0; }
  html, body { width: 1200px; height: 2340px; overflow: hidden; }
  body {
    background: var(--stage);
    position: relative;
    font-family: "Bebas Neue", "Oswald", sans-serif;
    color: var(--ink);
  }
  .flyer {
    position: absolute;
    left: 50px; top: 392px;
    width: 1100px; height: 1556px;
    background: radial-gradient(ellipse at 50% 40%, #ffffff 0%, var(--paper) 55%, var(--paper-shade) 100%);
    overflow: hidden;
    box-shadow: 0 20px 50px rgba(0,0,0,0.25);
  }
  .flyer > * { position: absolute; }
  .backdrop { left: 0; top: 0; width: 1100px; height: 1556px; }
  .brand {
    left: 0; width: 100%; top: 66px;
    display: flex; align-items: center; justify-content: center; gap: 18px;
    font-size: 64px; letter-spacing: 1px; color: var(--ink); line-height: 1;
  }
  .brand-dot { width: 56px; height: 56px; border-radius: 50%; background: var(--gold); }
  .script { font-family: "Playball", "Great Vibes", cursive; color: var(--gold); line-height: 1; }
  .title-grand {
    left: 0; width: 100%; top: 208px; text-align: center;
    font-size: 190px; color: var(--gold-deep);
    background: linear-gradient(180deg, #f2d33a 0%, #d6ab1c 100%);
    -webkit-background-clip: text; background-clip: text; -webkit-text-fill-color: transparent;
    z-index: 2; padding-left: 20px;
  }
  .title-opening {
    left: 0; width: 100%; top: 290px; text-align: center;
    font-size: 300px; line-height: 1; letter-spacing: 2px; color: var(--ink);
    text-shadow: 0 8px 14px rgba(0,0,0,0.12);
  }
  .title-opening .cap { font-size: 300px; }
  .title-opening .mid { font-size: 232px; }
  .label { left: 0; width: 100%; text-align: center; }
  .label-event { top: 590px; font-size: 72px; }
  .rule { height: 2px; background: var(--rule); }
  .rule-top { left: 224px; width: 650px; top: 672px; }
  .rule-bottom { left: 224px; width: 650px; top: 761px; }
  .event-date { left: 0; width: 100%; top: 680px; text-align: center; font-size: 86px; letter-spacing: 3px; line-height: 1; }
  .detail { width: 300px; text-align: center; }
  .detail-day { left: 263px; top: 776px; }
  .detail-time { left: 537px; top: 776px; }
  .detail .script { font-size: 44px; display: block; }
  .detail .value { font-size: 46px; letter-spacing: 1px; display: block; line-height: 1; margin-top: 2px; }
  .divider { left: 549px; top: 774px; width: 2px; height: 96px; background: var(--rule); }
  .label-location { top: 884px; font-size: 56px; }
  .address { left: 0; width: 100%; top: 952px; text-align: center; font-size: 28px; letter-spacing: 1px; }
  .rule-short { left: 497px; width: 106px; top: 1017px; height: 2px; background: var(--rule); }
  .photo {
    left: 40px; top: 1060px; width: 1020px; height: 496px;
    background: radial-gradient(ellipse at 40% 45%, #bcd7e6 0%, #e6eef2 45%, #f4f4f4 75%, rgba(244,244,244,0) 100%);
    border-radius: 48% 48% 0 0 / 30% 30% 0 0;
  }
  .web-pill {
    left: 373px; top: 1464px; width: 354px; height: 48px;
    background: var(--ink); border-radius: 24px;
    color: var(--gold); font-size: 24px; letter-spacing: 2px;
    display: flex; align-items: center; justify-content: center;
  }
</style>
</head>
<body>
  <main class="flyer">
    <svg class="backdrop" viewBox="0 0 1100 1556" aria-hidden="true">
      <g fill="none" stroke="#ffffff" stroke-width="3" opacity="0.9">
        <path d="M0 440 L340 0"/><path d="M0 520 L400 0"/>
        <path d="M1100 440 L760 0"/><path d="M1100 520 L700 0"/>
      </g>
      <path d="M0 1430 Q550 1000 1100 1430" fill="none" stroke="var(--gold-soft)" stroke-width="14"/>
    </svg>

    <div class="brand"><span class="brand-dot"></span><span class="brand-name">Stellar Motion Therapy</span></div>

    <h1 class="title-opening"><span class="cap">O</span><span class="mid">PENIN</span><span class="cap">G</span></h1>
    <div class="script title-grand">Grand</div>

    <div class="script label label-event">Event</div>
    <div class="rule rule-top"></div>
    <div class="event-date">June 1st, 2023</div>
    <div class="rule rule-bottom"></div>

    <div class="detail detail-day"><span class="script">Day</span><span class="value">Thursday</span></div>
    <div class="divider"></div>
    <div class="detail detail-time"><span class="script">Time</span><span class="value">12PM-6PM</span></div>

    <div class="script label label-location">Location</div>
    <div class="address">58274 Harlow Ave, Bloomfield Hills, MI 48319</div>
    <div class="rule-short"></div>

    <div class="photo" role="img" aria-label="Photo of a therapist in light blue scrubs assisting a smiling client seated in a white robotic shoulder therapy machine"></div>

    <div class="web-pill">www.stellarmotiontherapy.com</div>
  </main>
</body>
</html>
```